Election campaign for community-managed mental health sector - Webpage Banner and Logo

Please refer to the attached design brief for all the information and details. This is a campaign logo, and graphic design for the webpage banner.

Target Market(s)

Primary • NSW Ministers, Shadow Ministers, MPs and political advisers • Treasury and health policy decision-makers • Other key decision makers and stakeholders Secondary • Community-managed mental health workers • Sector leaders and advocates • People with lived experience and their families

Industry/Entity Type

Community-managed mental health sector in NSW, Australia

Other font styles liked:
• Meridian Sans Family

Requirements
Must have
• Please refer to design brief
Nice to have
Should not have
• Completely AI generated - see design brief for more information.

```html
<!DOCTYPE html>
<html lang="en">
<head>
<meta charset="utf-8">
<title>Steady Path Forward – Web Banner Concepts</title>
<link href="https://fonts.googleapis.com/css2?family=Montserrat:wght@500;600;700;800&family=PT+Sans&display=swap" rel="stylesheet">
<style>
  :root {
    --page: #e4e4e4;
    --purple: #512d7f;
    --orange: #f07d22;
    --green: #4aaa4a;
    --ink: #231f20;
    --white: #ffffff;
    --button: #ddd5ea;
    --button-ink: #3a2d52;
  }
  * { margin: 0; padding: 0; box-sizing: border-box; }
  html, body { width: 884px; height: 1200px; overflow: hidden; background: var(--page); }
  body { position: relative; font-family: "Montserrat", Arial, sans-serif; color: var(--ink); }

  .banner { position: absolute; width: 787px; height: 315px; overflow: hidden; }
  .banner--one { left: 46px; top: 42px; }
  .banner--two { left: 46px; top: 378px; }
  .banner--three { left: 42px; top: 715px; }
  .banner__backdrop { position: absolute; inset: 0; width: 100%; height: 100%; display: block; }
  .fill-purple { fill: var(--purple); }
  .fill-orange { fill: var(--orange); }
  .fill-white { fill: var(--white); }

  .ribbon { position: absolute; border-radius: 30px 30px 8px 8px; }
  .ribbon--duo {
    left: 49px; top: 53px; width: 114px; height: 164px;
    background: linear-gradient(135deg, var(--orange), var(--purple) 55%, var(--orange));
    opacity: .85;
  }
  .ribbon--green { width: 59px; height: 88px; background: var(--green); }
  .banner--two .ribbon--green { left: 437px; top: 48px; }
  .banner--three .ribbon--green { left: 437px; top: 49px; }

  .wordmark {
    position: absolute;
    font-weight: 800;
    color: var(--ink);
    line-height: 1;
    white-space: nowrap;
  }
  .wordmark--stacked { left: 414px; width: 280px; top: 86px; text-align: center; }
  .wordmark--stacked .wordmark__part { display: block; }
  .wordmark--stacked .wordmark__part--lead { font-size: 46px; }
  .wordmark--stacked .wordmark__part--mid { font-size: 27px; margin-top: 3px; }
  .wordmark--stacked .wordmark__part--end { font-size: 38px; margin-top: 3px; }

  .wordmark--inline {
    display: flex; align-items: center; justify-content: center; gap: 10px;
  }
  .banner--two .wordmark--inline { left: 256px; width: 420px; top: 140px; font-size: 37px; }
  .banner--three .wordmark--inline { left: 242px; width: 454px; top: 142px; font-size: 40px; gap: 14px; }
  .wordmark--inline .wordmark__part--mid { font-size: .5em; font-weight: 800; }

  .tagline {
    position: absolute;
    font-weight: 600;
    white-space: nowrap;
    text-align: center;
    color: var(--ink);
  }
  .banner--one .tagline { left: 380px; width: 350px; top: 235px; font-size: 13.5px; }
  .banner--two .tagline { left: 268px; width: 400px; top: 191px; font-size: 15.5px; }
  .banner--three .tagline { left: 242px; width: 460px; top: 193px; font-size: 17px; }

  .cta {
    position: absolute;
    width: 80px; height: 17px;
    border-radius: 9px;
    background: var(--button);
    color: var(--button-ink);
    font-size: 8.5px;
    font-weight: 500;
    display: flex; align-items: center; justify-content: center; gap: 3px;
  }
  .cta__arrow { width: 0; height: 0; border-left: 4px solid var(--ink); border-top: 3.5px solid transparent; border-bottom: 3.5px solid transparent; }
  .banner--one .cta { left: 68px; top: 250px; }
  .banner--two .cta { left: 427px; top: 222px; }
  .banner--three .cta { left: 429px; top: 225px; }

  .rationale {
    position: absolute;
    left: 52px; top: 1063px; width: 800px;
    font-family: "PT Sans", Arial, sans-serif;
    font-size: 18.5px;
    line-height: 24px;
    color: var(--ink);
  }
</style>
</head>
<body>

  <section class="banner banner--one">
    <svg class="banner__backdrop" viewBox="0 0 787 315" aria-hidden="true">
      <rect class="fill-purple" width="787" height="315"/>
      <path class="fill-orange" d="M522,0 L787,0 L787,315 L620,315 C400,305 230,270 216,215 C200,150 330,70 522,0 Z"/>
      <path class="fill-white" d="M642,0 L787,0 L787,271 C700,280 620,284 560,284 C400,284 300,262 293,218 C285,160 420,80 642,0 Z"/>
    </svg>
    <div class="ribbon ribbon--duo" role="img" aria-label="Awareness ribbon in orange and purple"></div>
    <a class="cta">Find out more<span class="cta__arrow"></span></a>
    <h1 class="wordmark wordmark--stacked">
      <span class="wordmark__part wordmark__part--lead">STEADY</span>
      <span class="wordmark__part wordmark__part--mid">PATH</span>
      <span class="wordmark__part wordmark__part--end">FORWARD</span>
    </h1>
    <p class="tagline">Putting community-based mental health care first</p>
  </section>

  <section class="banner banner--two">
    <svg class="banner__backdrop" viewBox="0 0 787 315" aria-hidden="true">
      <rect class="fill-purple" width="787" height="315"/>
      <path class="fill-orange" d="M317,0 L787,0 L787,315 L404,315 C180,300 40,260 37,197 C35,130 170,60 317,0 Z"/>
      <path class="fill-white" d="M432,0 L787,0 L787,235 L622,259 C540,268 450,273 366,273 C200,273 118,240 116,197 C114,140 260,70 432,0 Z"/>
    </svg>
    <div class="ribbon ribbon--green" role="img" aria-label="Green awareness ribbon"></div>
    <h2 class="wordmark wordmark--inline">
      <span class="wordmark__part">STEADY</span>
      <span class="wordmark__part wordmark__part--mid">PATH</span>
      <span class="wordmark__part">FORWARD</span>
    </h2>
    <p class="tagline">Putting community-based mental health care first</p>
    <a class="cta">Find out more<span class="cta__arrow"></span></a>
  </section>

  <section class="banner banner--three">
    <svg class="banner__backdrop" viewBox="0 0 787 315" aria-hidden="true">
      <rect class="fill-purple" width="787" height="315"/>
      <path class="fill-orange" d="M317,0 L787,0 L787,315 L404,315 C180,300 40,260 37,197 C35,130 170,60 317,0 Z"/>
      <path class="fill-white" d="M432,0 L787,0 L787,235 L622,259 C540,268 450,273 366,273 C200,273 118,240 116,197 C114,140 260,70 432,0 Z"/>
    </svg>
    <div class="ribbon ribbon--green" role="img" aria-label="Green awareness ribbon"></div>
    <h2 class="wordmark wordmark--inline">
      <span class="wordmark__part">STEADY</span>
      <span class="wordmark__part wordmark__part--mid">PATH</span>
      <span class="wordmark__part">FORWARD</span>
    </h2>
    <p class="tagline">Putting community-based mental health care first</p>
    <a class="cta">Find out more<span class="cta__arrow"></span></a>
  </section>

  <p class="rationale">
    The visual depicts cmhn branding graphic, with reversed Typography as the main concept<br>
    and a ribbon to stress cmhn commitment.<br>
    Ties well into the idea of community and care, puts community-based mental health care first.<br>
    Typography: Meridian Sans Font family
  </p>

</body>
</html>
```